Business Card design - 2 sides

I need a new business card design using our new branding.
On one side of the card I need to have our logo and my contact details et. On the otherside I need to display an offer to go to our website and order a copy of our free report.
If you visit my website www.kelbrookholdings.com.au you will see our logo and branding colours. You will also see an opt-in box with a picture of our free report and CD.
These are the details I would like on the front of the card
Logo: See attached logo file
Tag line:
Company Name: Kelbrook Holdings Australia
Name: Dennis Halloway
Title: Business Developer
Address:
Level 8, 54 Warrane Lane
Sydney NSW 2000
PO Box 4826 Brookvale
NSW 2100 Australia
Telephone: 1300 418 965
Mobile: 0431 906 273
Facsimile: 1300 418 966
Email: dennis.halloway@kelbrookholdings.com.au
Website: www.kelbrookholdings.com.au
These are the details to go on the backside of the card
Picture of Report and CD (see attached image file)
Offer:
ATTENTION: Importers and Exporters...
REVEALED AT LAST!! The 5 Critical Qualities Your Currency Exchange Provider Must Have!
Claim your complimentary copy of “The Quiet Owner's Handbook on
Lasting Overseas Payment Results”” (valued at $97)
Simply go to www.kelbrookholdings.com.au
Attachments: I have attached
1. PSD file of our Free report
2. PNG file of our logo (Main logo is blue and green lettering: Logo2)
3. PNG file of alternative logo, I'm not sure if this will be needed but included anyway (white and green lettering: Logo3)
Best regards,
Dennis
Business Owners and Financial Controllers of Import/Export companies.
Business

```html
<!DOCTYPE html>
<html lang="en">
<head>
<meta charset="utf-8">
<title>Kelbrook Holdings Australia – Business Card, Front and Back</title>
<link rel="stylesheet" href="https://fonts.googleapis.com/css2?family=Urbanist:wght@400;500;800&display=swap">
<style>
  :root {
    --page-bg: #e9ebed;
    --card-bg: #f7f7f6;
    --card-edge: #d9dbdd;
    --ink: #1f2124;
    --brand-navy: #1b3f7a;
    --brand-green: #8cc63f;
    --report-light: #f1f3f1;
    --report-mid: #c9d3cc;
  }

  * { box-sizing: border-box; margin: 0; padding: 0; }

  html, body {
    width: 1200px;
    height: 1000px;
    overflow: hidden;
    background: var(--page-bg);
    font-family: "Urbanist", "Century Gothic", sans-serif;
    color: var(--ink);
  }

  .sheet {
    width: 1200px;
    height: 1000px;
    display: flex;
    align-items: center;
    justify-content: center;
    gap: 60px;
  }

  .card {
    width: 520px;
    height: 840px;
    background: var(--card-bg);
    border: 1px solid var(--card-edge);
    box-shadow: 0 6px 18px rgba(0, 0, 0, 0.08);
    display: flex;
    flex-direction: column;
  }

  /* ---------- Front ---------- */
  .card-front { padding: 150px 40px 56px; }

  .brand-mark {
    display: flex;
    align-items: center;
    gap: 14px;
  }
  .brand-mark__dot {
    flex: none;
    width: 28px;
    height: 28px;
    border-radius: 50%;
    background: var(--brand-green);
  }
  .brand-mark__name {
    font-size: 46px;
    font-weight: 500;
    color: var(--brand-navy);
    line-height: 1;
    white-space: nowrap;
  }

  .identity {
    margin-top: 30px;
    font-size: 19px;
    line-height: 1.15;
  }
  .identity__company,
  .identity__person { font-weight: 800; }

  .contact {
    margin-top: auto;
    font-size: 19px;
    line-height: 1.15;
  }
  .contact address { font-style: normal; }
  .contact__phones { margin-top: 22px; }
  .contact__online { margin-top: 22px; white-space: nowrap; }

  /* ---------- Back ---------- */
  .card-back { padding: 52px 40px 52px; }

  .offer__headline {
    font-size: 17px;
    font-weight: 800;
    line-height: 1.35;
  }
  .offer__text {
    margin-top: 14px;
    font-size: 17px;
    line-height: 1.45;
  }

  .report-visual {
    margin: 40px 0 0 auto;
    width: 260px;
    height: 200px;
    background: linear-gradient(135deg, var(--report-light) 0%, var(--report-mid) 60%, var(--brand-green) 100%);
    border: 1px solid var(--card-edge);
  }

  .offer__cta {
    margin-top: auto;
    font-size: 19px;
    white-space: nowrap;
  }
</style>
</head>
<body>
<main class="sheet">

  <section class="card card-front" aria-label="Business card front">
    <div class="brand-mark">
      <span class="brand-mark__dot"></span>
      <span class="brand-mark__name">Kelbrook Holdings</span>
    </div>

    <div class="identity">
      <p class="identity__company">Kelbrook Holdings Australia</p>
      <p class="identity__person">Dennis Halloway</p>
      <p class="identity__title">Business Developer</p>
    </div>

    <div class="contact">
      <address>
        <p>Level 8, 54 Warrane Lane</p>
        <p>Sydney NSW 2000</p>
        <p>PO Box 4826 Brookvale</p>
        <p>NSW 2100 Australia</p>
      </address>

      <div class="contact__phones">
        <p>t: 1300 418 965</p>
        <p>m: 0431 906 273</p>
        <p>f: 1300 418 966</p>
      </div>

      <div class="contact__online">
        <p>e: dennis.halloway@kelbrookholdings.com.au</p>
        <p>w: www.kelbrookholdings.com.au</p>
      </div>
    </div>
  </section>

  <section class="card card-back" aria-label="Business card back">
    <div class="offer">
      <p class="offer__headline">ATTENTION: Importers and Exporters...<br>REVEALED AT LAST!!</p>
      <p class="offer__text">The 5 Critical Qualities Your Currency Exchange Provider Must Have!</p>
      <p class="offer__text">Claim your complimentary copy of “The Quiet Owner's Handbook on Lasting Overseas Payment Results” (valued at $97)</p>
    </div>

    <div class="report-visual" role="img" aria-label="Free report cover alongside its companion CD"></div>

    <p class="offer__cta">Simply go to www.kelbrookholdings.com.au</p>
  </section>

</main>
</body>
</html>
```